Brighten Your Calling - book web site

I need a web site for my book that is being published and will be available on Tellurio April 6th. It will have an email opt in which will then email the person a pdf report.
And it will have a bio page.
My logo, pic, book cover and bio details are attached below.

Target Market(s)

New life coaches that are looking to figure out their purpose and branding for their business

Industry/Entity Type

Life Coaching

Number of Pages Required

3 page

Font styles to use
Serif

Requirements
Must have
• The book cover, my logo, an opt in page, a bio page, my picture
• i would like the book in the header
• Needs to be chatterloop compliant
Should not have
• except for the logo, willow heart and soul will NOT be highlighted in the header

```html
<!DOCTYPE html>
<html lang="en">
<head>
<meta charset="utf-8">
<title>Brighten Your Calling – Maren Holloway</title>
<link href="https://fonts.googleapis.com/css2?family=Lora:wght@400;500;600;700&display=swap" rel="stylesheet">
<style>
  :root {
    --ink: #111111;
    --white: #ffffff;
    --logo: #d9822b;
    --hero-dark: #4e4841;
    --hero-mid: #7d6e60;
    --hero-light: #9a8878;
    --contact-dark: #6f675e;
    --contact-mid: #9a8e80;
    --contact-light: #b9ad9f;
    --cover-deep: #3f8f7c;
    --cover-light: #8fd3b8;
    --photo-bg: #a9a9a9;
    --photo-deep: #4a3a33;
    --field: #c6c6c6;
    --contact-label: #ece8e2;
  }
  * { box-sizing: border-box; margin: 0; padding: 0; }
  html, body { width: 1200px; height: 2242px; overflow: hidden; background: var(--white); }
  body { position: relative; font-family: "Lora", Georgia, serif; color: var(--ink); }

  .site-header { position: absolute; left: 0; top: 0; width: 1200px; height: 100px; }
  .brand { position: absolute; left: 84px; top: 38px; display: flex; align-items: center; gap: 6px;
    font-size: 13px; font-weight: 600; color: var(--logo); letter-spacing: 0.5px; }
  .brand-dot { width: 14px; height: 14px; border-radius: 50%; background: var(--logo); }
  .main-nav { position: absolute; right: 43px; top: 34px; display: flex; gap: 12px;
    font-size: 23px; font-weight: 700; }

  .hero { position: absolute; left: 50px; top: 106px; width: 1108px; height: 564px; overflow: hidden; }
  .hero-backdrop { position: absolute; inset: 0;
    background: linear-gradient(100deg, var(--hero-dark) 0%, var(--hero-mid) 45%, var(--hero-light) 100%); }
  .hero-title { position: absolute; left: 28px; top: 206px; width: 520px;
    font-size: 45px; line-height: 46px; font-weight: 700; letter-spacing: 5px; color: var(--white); }
  .hero-release { position: absolute; left: 28px; top: 374px;
    font-size: 25px; font-weight: 700; letter-spacing: 3px; color: var(--white); }
  .book-cover { position: absolute; left: 720px; top: 60px; width: 300px; height: 446px;
    background: radial-gradient(ellipse at 50% 45%, var(--cover-light), var(--cover-deep)); }

  .bio-heading { position: absolute; left: 0; top: 754px; width: 1232px; text-align: center;
    font-size: 33px; font-weight: 600; }
  .portrait { position: absolute; left: 78px; top: 834px; width: 498px; height: 609px;
    background: linear-gradient(180deg, var(--photo-bg) 0 55%, var(--photo-deep) 100%); }
  .bio-text { position: absolute; font-size: 20px; line-height: 28.5px; font-weight: 600; letter-spacing: 1.3px; }
  .bio-side { left: 628px; width: 510px; }
  .bio-wide { left: 78px; width: 1062px; }

  .contact { position: absolute; left: 50px; top: 1833px; width: 1108px; height: 375px; overflow: hidden; }
  .contact-backdrop { position: absolute; inset: 0;
    background: linear-gradient(90deg, var(--contact-dark) 0%, var(--contact-mid) 45%, var(--contact-light) 100%); }
  .contact-title { position: absolute; left: 0; top: 26px; width: 1108px; text-align: center;
    font-size: 33px; font-weight: 600; letter-spacing: 4px; color: var(--white); }
  .contact-lead { position: absolute; left: 0; top: 74px; width: 1108px; text-align: center;
    font-size: 21px; font-weight: 700; letter-spacing: 1.5px; color: var(--white); }
  .field { position: absolute; left: 0; display: flex; align-items: center; }
  .field label { width: 522px; text-align: right; padding-right: 30px;
    font-size: 21px; font-weight: 700; color: var(--contact-label); }
  .field-input { height: 34px; background: var(--field); border: 0; }
  .field-short .field-input { width: 192px; }
  .field-long .field-input { width: 365px; }
  .send-button { position: absolute; left: 450px; top: 298px; width: 215px; height: 40px;
    background: var(--white); border: 2px solid var(--ink); font-family: "Lora", Georgia, serif;
    font-size: 25px; font-weight: 700; color: var(--ink); }
</style>
</head>
<body>
  <header class="site-header">
    <div class="brand"><span class="brand-dot"></span>Willow Heart and Soul</div>
    <nav class="main-nav"><span>Who is Maren</span><span>Contact</span></nav>
  </header>

  <section class="hero">
    <div class="hero-backdrop" role="img" aria-label="Background photo of a writer's wooden desk"></div>
    <h1 class="hero-title">Brighten Your Calling And Grow Your Business</h1>
    <p class="hero-release">Available on Tellurio on April 6th</p>
    <div class="book-cover" role="img" aria-label="Book cover of Brighten Your Calling by Maren Holloway"></div>
  </section>

  <h2 class="bio-heading">Who is Maren</h2>
  <div class="portrait" role="img" aria-label="Portrait photo of the author, Maren Holloway"></div>

  <p class="bio-text bio-side" style="top:828px">Maren Holloway, founder of Willow Heart and Soul, helps new coaches and creative entrepreneurs find their inner voice so that they have the confidence to bring their authentic selves out into the world.</p>
  <p class="bio-text bio-side" style="top:1016px">Maren’s keen sense of what works is backed by a thorough education in psychology, health, nutrition, training and management. She’s a certified health counselor, having trained at the Academy of Whole Health in New York (accredited by Easton Teachers College).</p>
  <p class="bio-text bio-side" style="top:1276px">She holds a bachelor’s degree in psychology from Harborview University, giving her a deep understanding of the motivations behind food, career and lifestyle choices. She spent a decade in management with some of the most successful food businesses in the country.</p>
  <p class="bio-text bio-wide" style="top:1496px">Maren has helped businesses achieve dramatic improvements in their organization and focus – in turn, making their businesses more profitable. Clients who seek Maren’s guidance are ready to get real and get wise, both in terms of health and business goals. She helps coaches quickly recognize easy to integrate strategies that will suit their work style to help eliminate the confusion on what to do next which in turn will boost their confidence and their bottom line.</p>
  <p class="bio-text bio-wide" style="top:1679px">Maren is a classically trained culinary chef from Larchmont Culinary Institute and a certified raw foods chef, a certified yoga instructor, reiki master, a StillPoint facilitator, and a certified Business Coach for Wellness and Artistic Professionals.</p>

  <section class="contact">
    <div class="contact-backdrop" role="img" aria-label="Faded background photo of a writer's wooden desk"></div>
    <h2 class="contact-title">Contact the Author</h2>
    <p class="contact-lead">Email me and I will send you a pdf report.</p>
    <div class="field field-short" style="top:124px"><label>First Name</label><div class="field-input"></div></div>
    <div class="field field-short" style="top:177px"><label>Last Name</label><div class="field-input"></div></div>
    <div class="field field-long" style="top:232px"><label>Email Address</label><div class="field-input"></div></div>
    <button class="send-button" type="button">SEND</button>
  </section>
</body>
</html>
```